Bright Quest Appeal needs a brochure

I need an A4 - Two sided brochure design.
It's for a maths challenge fundraiser for primary schools throughout Australia.
It needs to be bright and fun with the pictures / files supplied,
Please use as many pics as you can, more the better...
Also keep Logos as transparent
See our website for an idea of what we do pls. thebrightquest.example
Pls make it FUN ....NOT corporate..
so curves and colours rather than straight lines
The only headings that need to be ALL capitals is "FREE TO JOIN" & "FUNDRAISER" Other titles not all capitals pls
Please note: when putting in the pics of the games, pls put in order from game1-7 as they go in order of the school grade levels (Preschool to Grade 6). showing teachers how they become more difficult...in that order.
This brochure will be sent to schools.
Schools have admin open letters, we get about 2 - 3 seconds for admin to decide to keep or bin the brochure, so they need to see it's a fundraiser and "free to join" in those seconds.
cheers
- fun style maybe marker felt or comic sans but you choose any other you think works to make it fun

```html
<!DOCTYPE html>
<html lang="en">
<head>
<meta charset="utf-8">
<title>Bright Quest Appeal – Maths Challenge Brochure</title>
<link href="https://fonts.googleapis.com/css2?family=Lilita+One&family=Itim&family=Montserrat:wght@400&display=swap" rel="stylesheet">
<style>
  :root{
    --navy:#1b2f57;
    --aqua:#8fdcd6;
    --white:#ffffff;
    --ink:#222831;
    --stage:#f2f2f2;
    --gold:#d9a93a;
  }
  *{box-sizing:border-box;margin:0;padding:0}
  html,body{width:1200px;height:852px;overflow:hidden;background:var(--stage)}
  .canvas{position:relative;width:1200px;height:852px}
  .page{position:absolute;top:68px;width:505px;height:715px;overflow:hidden}
  .page--front{left:70px;background:var(--white)}
  .page--back{left:625px;background:var(--navy)}
  .abs{position:absolute}
  .display{font-family:"Lilita One",cursive}
  .body{font-family:"Itim",cursive}

  /* front */
  .brand{left:0;width:505px;top:40px;display:flex;justify-content:center;align-items:center;gap:8px;font-family:"Lilita One",cursive;font-size:26px;color:var(--navy)}
  .brand-dot{width:18px;height:18px;border-radius:50%;background:#e32b2b}
  .tagline{left:0;width:505px;top:104px;text-align:center;font-family:"Montserrat",sans-serif;font-size:11.5px;color:var(--ink)}
  .navy-band{left:0;top:430px;width:505px;height:285px;background:var(--navy)}
  .hero{left:0;top:128px;width:505px;height:390px}
  .hero-title{left:0;width:505px;text-align:center;color:var(--white);z-index:2}
  .t-maths{top:170px;font-size:24px;line-height:1}
  .t-challenge{top:196px;font-size:25px;line-height:1}
  .t-fundraiser{top:230px;font-size:46px;line-height:1;letter-spacing:-.5px}
  .hero-quote{left:0;width:505px;top:282px;text-align:center;font-family:"Itim",cursive;font-style:italic;font-size:13px;line-height:15px;color:var(--white);z-index:2}
  .photo{border-radius:50%;border:3px solid var(--white)}
  .front-copy{left:22px;color:var(--white)}
  .h-sub{font-size:17px;line-height:1}
  .p-copy{font-size:13px;line-height:14.5px}
  .certificate{left:387px;top:572px;width:86px;height:120px;background:var(--white);padding:3px}
  .certificate div{width:100%;height:100%;background:linear-gradient(135deg,#f3d27a,var(--gold) 60%,#b8862a)}

  /* back */
  .aqua-h{color:var(--aqua);font-size:16.5px;line-height:19px}
  .bullets{list-style:none;color:var(--white);font-family:"Itim",cursive;font-size:10.5px;line-height:12.5px}
  .bullets li{position:relative;padding-left:18px}
  .bullets li::before{content:"";position:absolute;left:3px;top:4px;width:5px;height:5px;border-radius:50%;background:var(--aqua)}
  .pill{left:23px;top:239px;height:20px;padding:0 10px;border-radius:10px;background:var(--aqua);color:var(--navy);font-size:13px;line-height:20px}
  .white-band{left:0;top:470px;width:505px;height:245px;background:var(--white)}
  .navy-h{color:var(--navy);font-size:15.5px;line-height:17px}
  .game{width:56px;height:41px;border-radius:4px}
  .contact{left:311px;color:var(--navy);display:flex;align-items:center;gap:8px}
  .contact svg{flex:none}
  .partner{left:407px;top:522px;width:66px;text-align:center;font-family:"Itim",cursive;font-size:8px;color:var(--ink)}
  .partner-mark{width:38px;height:38px;margin:0 auto 4px;border-radius:50%;background:var(--navy)}
</style>
</head>
<body>
<main class="canvas">

  <!-- FRONT PAGE -->
  <section class="page page--front" aria-label="Brochure front">
    <div class="abs brand"><span class="brand-dot"></span>Bright Quest</div>
    <p class="abs tagline">Fun games developing confidence in mathematics.</p>

    <div class="abs navy-band"></div>

    <svg class="abs hero" viewBox="0 0 505 390" role="img" aria-label="Chalkboard with maths doodles and a cheering schoolgirl holding a sponge">
      <defs>
        <radialGradient id="chalk" gradientUnits="userSpaceOnUse" cx="255" cy="170" r="260">
          <stop offset="0" stop-color="#474d55"/>
          <stop offset="1" stop-color="#1c2026"/>
        </radialGradient>
      </defs>
      <g fill="var(--aqua)">
        <circle cx="165" cy="105" r="98"/>
        <circle cx="250" cy="110" r="100"/>
        <circle cx="330" cy="115" r="90"/>
        <circle cx="410" cy="175" r="80"/>
        <circle cx="95" cy="205" r="82"/>
        <circle cx="255" cy="215" r="150"/>
        <circle cx="390" cy="260" r="90"/>
      </g>
      <g fill="url(#chalk)">
        <circle cx="165" cy="105" r="90"/>
        <circle cx="250" cy="110" r="92"/>
        <circle cx="330" cy="115" r="82"/>
        <circle cx="410" cy="175" r="72"/>
        <circle cx="95" cy="205" r="74"/>
        <circle cx="255" cy="215" r="142"/>
        <circle cx="390" cy="260" r="82"/>
      </g>
    </svg>

    <div class="abs hero-title display t-maths">Maths</div>
    <div class="abs hero-title display t-challenge">Challenge</div>
    <div class="abs hero-title display t-fundraiser">FUNDRAISER</div>
    <p class="abs hero-quote">“A great fundraiser helping primary school<br>students with maths!”</p>

    <div class="abs photo" role="img" aria-label="Two excited children at a laptop" style="left:26px;top:382px;width:170px;height:145px;border-radius:48% 52% 46% 54%;background:radial-gradient(circle at 45% 40%,#8a9a7a,#3d4a45)"></div>
    <div class="abs photo" role="img" aria-label="Classmates high-fiving beside a laptop" style="left:305px;top:440px;width:185px;height:122px;border-radius:50%;background:radial-gradient(circle at 40% 45%,#d8dde4,#6f8cad)"></div>

    <div class="abs front-copy" style="top:533px">
      <h2 class="display h-sub">Students love a challenge !</h2>
      <p class="body p-copy" style="margin-top:6px">Students are challenged to solve educational<br>maths games on The Bright Quest website.</p>
    </div>
    <div class="abs front-copy" style="top:600px">
      <h2 class="display h-sub">It’s lots of fun and helps students with maths !</h2>
      <p class="body p-copy" style="margin-top:7px">The maths challenge is designed to build confidence in<br>mathematics for primary school students.</p>
      <p class="body p-copy" style="margin-top:12px">Once students have completed their maths challenge, they<br>may download a certificate of congratulations.</p>
    </div>
    <div class="abs certificate" role="img" aria-label="Gold certificate of congratulations"><div></div></div>
  </section>

  <!-- BACK PAGE -->
  <section class="page page--back" aria-label="Brochure back">
    <div class="abs display aqua-h" style="left:23px;top:18px">FREE TO JOIN !<br><span style="display:block;margin-top:5px">Effortless to run !</span></div>
    <ul class="abs bullets" style="left:23px;top:70px;width:460px">
      <li>It’s all set-up online and ready to go. No spending time or effort planning activities or fundraiser days.</li>
      <li style="margin-top:11px">The Bright Quest website is fully safe and secure with no information sharing, no links to other sites and no popup advertising.</li>
      <li style="margin-top:11px">Plus, all Bright Quest games are aligned with the Australian Mathematics Curriculum.</li>
    </ul>
    <div class="abs display aqua-h" style="left:24px;top:171px">All set up online for you !<br>Builds confidence in maths for students !<br>Easy to run !</div>
    <div class="abs pill display">Here is how it works:</div>
    <ul class="abs bullets" style="left:23px;top:269px;width:460px">
      <li>Let us know how many memberships you need for your Bright Quest Appeal.</li>
      <li style="margin-top:9px">We will send you our website access code for those memberships.</li>
      <li style="margin-top:8px">Download our fundraising letter, photocopy and give to parents to collect funds.<br>(See our website for more details.)</li>
      <li style="margin-top:8px">On the website, each year level has a set of maths challenges for students to solve.</li>
      <li style="margin-top:9px">Once completed students may download a certificate of congratulations.</li>
    </ul>

    <div class="abs white-band"></div>
    <svg class="abs" style="left:0;top:440px" width="505" height="60" viewBox="0 0 505 60" aria-hidden="true">
      <path d="M0 30 Q60 10 120 32 T250 30 T380 34 T505 22 V60 H0Z" fill="var(--white)"/>
    </svg>
    <div class="abs photo" role="img" aria-label="Grandmother helping a girl at a computer" style="left:35px;top:394px;width:204px;height:132px;border-radius:48% 52% 50% 50%;background:radial-gradient(circle at 50% 45%,#c9d6e4,#5f7896)"></div>
    <div class="abs photo" role="img" aria-label="Smiling students working at classroom computers" style="left:260px;top:394px;width:204px;height:132px;border-radius:50% 48% 52% 50%;background:radial-gradient(circle at 50% 45%,#d6b98a,#5b4c45)"></div>

    <div class="abs display navy-h" style="left:23px;top:558px">Over 260 maths games for<br>Foundation to Grade 6 !</div>
    <div class="abs game" role="img" aria-label="Game 1 screenshot" style="left:23px;top:602px;background:linear-gradient(135deg,#3a3fa8,#c9344a)"></div>
    <div class="abs game" role="img" aria-label="Game 2 screenshot" style="left:86px;top:602px;background:linear-gradient(135deg,#6fa6e0,#2d5da8)"></div>
    <div class="abs game" role="img" aria-label="Game 3 screenshot" style="left:149px;top:602px;background:linear-gradient(135deg,#7cc94a,#2f8c3a)"></div>
    <div class="abs game" role="img" aria-label="Game 4 screenshot" style="left:212px;top:602px;background:linear-gradient(135deg,#2e6fd0,#e0a62a)"></div>
    <div class="abs game" role="img" aria-label="Game 5 screenshot" style="left:57px;top:650px;background:linear-gradient(135deg,#3b7bd8,#1d3f8a)"></div>
    <div class="abs game" role="img" aria-label="Game 6 screenshot" style="left:119px;top:650px;background:linear-gradient(135deg,#1f3550,#0d1a2a)"></div>
    <div class="abs game" role="img" aria-label="Game 7 screenshot" style="left:182px;top:650px;background:linear-gradient(135deg,#3c3f44,#1c1e22)"></div>

    <div class="abs display" style="left:317px;top:546px;font-size:12px;color:var(--ink)">Promoted by:</div>
    <div class="abs partner"><div class="partner-mark"></div>Schoolfund Partners</div>

    <div class="abs display navy-h" style="left:311px;top:587px">Start a Maths Challenge<br>for your school:</div>
    <div class="abs contact" style="top:634px">
      <svg width="16" height="16" viewBox="0 0 16 16" aria-hidden="true"><circle cx="8" cy="8" r="8" fill="var(--aqua)"/><path d="M5.2 4.5l1.4-.3.8 1.9-.9.7a5 5 0 002.7 2.7l.7-.9 1.9.8-.3 1.4c-3.6.3-6.6-2.7-6.3-6.3z" fill="var(--navy)"/></svg>
      <span class="display" style="font-size:17px">1300 555 014</span>
    </div>
    <div class="abs contact body" style="top:658px;font-size:11px">
      <svg width="14" height="14" viewBox="0 0 16 16" aria-hidden="true"><circle cx="8" cy="8" r="8" fill="var(--aqua)"/><rect x="4" y="5" width="8" height="6" fill="none" stroke="var(--navy)" stroke-width="1.2"/><path d="M4 5l4 3.5L12 5" fill="none" stroke="var(--navy)" stroke-width="1.2"/></svg>
      <span>info@thebrightquest.example</span>
    </div>
    <div class="abs contact body" style="top:677px;font-size:11px">
      <svg width="14" height="14" viewBox="0 0 16 16" aria-hidden="true"><circle cx="8" cy="8" r="8" fill="var(--aqua)"/><circle cx="8" cy="8" r="4" fill="none" stroke="var(--navy)" stroke-width="1.1"/><path d="M4 8h8M8 4c-2 2.5-2 5.5 0 8M8 4c2 2.5 2 5.5 0 8" fill="none" stroke="var(--navy)" stroke-width="1"/></svg>
      <span>www.thebrightquest.example</span>
    </div>
  </section>

</main>
</body>
</html>
```